Wedding on the paradise

We are getting married in Koh Samui Thailand and need booklet/ concertina that contains the invitation, event program (Day 1 Sunset Cocktail Party, Day 2 Wedding Day, Day 4 Sunset Cruise) and information about the island of Koh Samui.

Also looking for the Wedding Day Program, Menu and card containing guest names.

Below is the link to my favorite invitation and would like similar outcome.

http://www.morvalstudio.com/wedding/couture.php?c=styles&s=destination&p=tasha_brenor

We have international guests and therefore require text in Mongolian and English.

Industry/Entity Type

Wedding

Colors
cedeec

```html
<!DOCTYPE html>
<html lang="en">
<head>
<meta charset="utf-8">
<title>Mira &amp; Tomas Wedding Invitation</title>
<link href="https://fonts.googleapis.com/css2?family=Bebas+Neue&family=Open+Sans:wght@400;600;700&display=swap" rel="stylesheet">
<style>
  :root {
    --berry: #9a3d5e;
    --berry-light: #b8607f;
    --plum-text: #9b2a63;
    --ink: #1f1f1f;
    --petal: #f08cb4;
    --petal-mid: #f4a6c5;
    --petal-soft: #fbe4ee;
    --petal-wash: #f9d4e3;
    --leaf: #a9bf92;
    --sage-bg: #e8ede0;
    --white: #ffffff;
  }
  * { box-sizing: border-box; margin: 0; padding: 0; }
  html, body { width: 1200px; height: 1000px; overflow: hidden; background: var(--white); }
  body { position: relative; font-family: "Open Sans", Arial, sans-serif; color: var(--ink); }

  .sheet-title {
    position: absolute; top: 38px; left: 0; width: 1200px; text-align: center;
    font-family: "Bebas Neue", Impact, sans-serif; font-weight: 400; font-size: 44px;
    letter-spacing: 0.5px; color: var(--berry); line-height: 1;
  }

  .card {
    position: absolute; width: 380px; height: 377px; overflow: hidden;
    background: var(--white); box-shadow: 0 2px 10px rgba(0,0,0,0.35);
  }
  .card--invite  { left: 20px;  top: 148px; }
  .card--welcome { left: 405px; top: 148px; }
  .card--wedding { left: 791px; top: 148px; }
  .card--friday  { left: 20px;  top: 552px; }
  .card--cruise  { left: 405px; top: 552px; }
  .card--info    { left: 791px; top: 552px; }

  .floral-frame {
    position: absolute; inset: 0;
    background:
      radial-gradient(circle at 15% 15%, var(--petal) 0 12%, transparent 22%),
      radial-gradient(circle at 85% 12%, var(--petal) 0 12%, transparent 22%),
      radial-gradient(circle at 12% 85%, var(--petal) 0 12%, transparent 22%),
      radial-gradient(circle at 85% 85%, var(--petal) 0 12%, transparent 22%),
      radial-gradient(circle at 50% 95%, var(--petal-mid) 0 10%, transparent 20%),
      radial-gradient(circle at 92% 50%, var(--petal-mid) 0 9%, transparent 18%),
      radial-gradient(circle at 8% 50%, var(--petal-mid) 0 9%, transparent 18%),
      var(--sage-bg);
  }
  .floral-wash {
    position: absolute; inset: 0;
    background:
      radial-gradient(circle at 20% 20%, var(--petal-wash) 0 10%, transparent 25%),
      radial-gradient(circle at 80% 30%, var(--petal-wash) 0 10%, transparent 25%),
      radial-gradient(circle at 25% 80%, var(--petal-wash) 0 10%, transparent 25%),
      radial-gradient(circle at 78% 82%, var(--petal-wash) 0 10%, transparent 25%),
      var(--petal-soft);
  }
  .center-disc { position: absolute; border-radius: 50%; background: var(--white); }
  .center-disc--soft { background: rgba(255,255,255,0.72); }

  .bud {
    position: absolute; border-radius: 50% 50% 45% 45%;
    background: radial-gradient(circle at 45% 40%, var(--petal) 0 45%, var(--leaf) 70%, transparent 72%);
  }
  .bouquet {
    position: absolute; border-radius: 50%;
    background: radial-gradient(circle at 50% 40%, var(--petal) 0 40%, var(--petal-mid) 55%, var(--leaf) 68%, transparent 72%);
  }
  .boat-art {
    position: absolute; left: 135px; top: 73px; width: 138px; height: 80px;
    border-radius: 6px;
    background: linear-gradient(180deg, var(--berry-light), var(--berry));
  }

  .content { position: absolute; left: 0; width: 100%; text-align: center; }
  .display { font-family: "Bebas Neue", Impact, sans-serif; font-weight: 400; color: var(--berry); line-height: 1; }

  /* invitation */
  .invite-lead { top: 156px; font-size: 13px; color: var(--plum-text); }
  .invite-names { top: 172px; font-size: 19px; font-weight: 700; color: var(--plum-text); }
  .invite-ask { top: 196px; font-size: 12px; color: var(--plum-text); }
  .invite-fine { top: 218px; font-size: 7.5px; line-height: 1.25; color: var(--ink); }
  .invite-fine .gap { display: block; height: 6px; }

  /* welcome */
  .welcome-title { top: 96px; font-size: 68px; }
  .welcome-body { top: 160px; padding: 0 36px; font-size: 13px; line-height: 1.52; }
  .welcome-sign { display: block; padding-left: 110px; }

  /* wedding day */
  .wedding-title { top: 108px; font-size: 52px; }
  .wedding-lines { top: 160px; font-size: 12.8px; line-height: 1.5; }
  .wedding-time { display: block; font-size: 18px; font-weight: 700; color: var(--berry); margin: 2px 0; }
  .wedding-time--late { margin-top: 8px; }

  /* friday */
  .friday-day { top: 116px; font-size: 42px; }
  .friday-date { top: 155px; font-size: 33px; }
  .friday-event { top: 207px; font-size: 14px; font-weight: 700; color: var(--berry); }
  .friday-body { top: 227px; font-size: 12.8px; line-height: 1.45; padding: 0 48px; }
  .friday-venue { top: 267px; font-size: 15px; font-weight: 700; color: var(--berry); }

  /* cruise */
  .cruise-title { top: 172px; font-size: 45px; }
  .cruise-sub { top: 213px; font-size: 16.5px; font-weight: 700; color: var(--berry); }

  /* info */
  .info-title { top: 18px; font-size: 42px; }
  .info-list { position: absolute; top: 50px; left: 17px; right: 12px; font-size: 12.8px; line-height: 1.42; }
  .info-head { font-weight: 700; color: var(--berry); }
  .info-text { text-indent: 40px; text-align: justify; hyphens: auto; -webkit-hyphens: auto; }
  .info-link { font-weight: 700; color: var(--berry); }

  .icon { position: absolute; }
</style>
</head>
<body>

<h1 class="sheet-title">Mira &amp; Tomas Wedding Invitation</h1>

<section class="card card--invite">
  <div class="floral-frame" role="img" aria-label="Frame of pink peony blossoms with green leaves"></div>
  <div class="center-disc" style="left:38px; top:96px; width:305px; height:290px;"></div>
  <div class="bud" role="img" aria-label="Small pink rosebud on a stem" style="left:178px; top:120px; width:26px; height:24px;"></div>
  <p class="content invite-lead">Together with their parents</p>
  <p class="content invite-names">Mira &amp; Tomas</p>
  <p class="content invite-ask">would like to invite</p>
  <p class="content invite-fine">
    Saturday, December 13, 2014<br>
    Ceremony at four o'clock in the afternoon
    <span class="gap"></span>
    to celebrate their union.<br>
    Baan Sala Lipa Noi Koh Samui
  </p>
</section>

<section class="card card--welcome">
  <div class="floral-wash" role="img" aria-label="Faint pink peony pattern background"></div>
  <div class="center-disc center-disc--soft" style="left:22px; top:25px; width:336px; height:320px;"></div>
  <div class="bouquet" role="img" aria-label="Small cluster of pink peonies" style="left:168px; top:42px; width:48px; height:56px;"></div>
  <h2 class="content display welcome-title">Welcome</h2>
  <p class="content welcome-body">
    To our family and friends, it means the world to us to have you here. Thank you for the support, love and laughter you have contributed to our lives. We hope you enjoy and relax your time in Koh Samui. Here is the weekend full of LOVE.
    <span class="welcome-sign">Mira &amp; Tom</span>
  </p>
</section>

<section class="card card--wedding">
  <div class="floral-frame" role="img" aria-label="Frame of pink peony blossoms with green leaves"></div>
  <div class="center-disc" style="left:35px; top:30px; width:330px; height:320px;"></div>
  <div class="bouquet" role="img" aria-label="Small cluster of pink peonies" style="left:50px; top:40px; width:44px; height:50px;"></div>
  <div class="bouquet" role="img" aria-label="Small cluster of pink peonies" style="left:265px; top:40px; width:44px; height:50px;"></div>
  <h2 class="content display wedding-title">Wedding Day</h2>
  <p class="content wedding-lines">
    Ceremony at
    <span class="wedding-time">5 PM</span>
    followed by celebration<br>
    Transportation from Bo Phut departing from
    <span class="wedding-time wedding-time--late">3.45 PM</span>
  </p>
</section>

<section class="card card--friday">
  <div class="floral-wash" role="img" aria-label="Faint pink peony pattern background"></div>
  <div class="center-disc center-disc--soft" style="left:22px; top:25px; width:336px; height:320px;"></div>
  <svg class="icon" style="left:160px; top:52px;" width="56" height="56" viewBox="0 0 56 56" role="img" aria-label="Cocktail glass icon">
    <g fill="none" stroke="var(--berry)" stroke-width="3">
      <rect x="4" y="12" width="40" height="40"/>
      <line x1="4" y1="22" x2="44" y2="22"/>
      <polyline points="34,22 34,6 44,2"/>
      <circle cx="16" cy="36" r="7"/>
    </g>
    <g stroke="var(--berry)" stroke-width="1.5">
      <line x1="16" y1="29" x2="16" y2="43"/>
      <line x1="9" y1="36" x2="23" y2="36"/>
    </g>
    <g fill="var(--berry)">
      <rect x="27" y="27" width="6" height="6"/>
      <rect x="33" y="38" width="6" height="6"/>
      <rect x="24" y="42" width="4" height="4"/>
    </g>
  </svg>
  <svg class="icon" style="left:228px; top:50px;" width="22" height="22" viewBox="0 0 22 22" role="img" aria-label="Sun icon">
    <g stroke="var(--berry)" stroke-width="1.4" fill="none">
      <circle cx="11" cy="11" r="4.5"/>
      <path d="M11 1v3M11 18v3M1 11h3M18 11h3M4 4l2 2M16 16l2 2M4 18l2-2M16 6l2-2"/>
    </g>
  </svg>
  <h2 class="content display friday-day">Friday</h2>
  <h3 class="content display friday-date">December 12</h3>
  <p class="content friday-event">Sunset Cocktail</p>
  <p class="content friday-body">At the first day with us, we relax, sip cocktail by the pool and enjoy beautiful Koh Samui.</p>
  <p class="content friday-venue">Baan Sala 3pm</p>
</section>

<section class="card card--cruise">
  <div class="floral-wash" role="img" aria-label="Faint pink peony pattern background"></div>
  <div class="center-disc center-disc--soft" style="left:22px; top:25px; width:336px; height:320px;"></div>
  <div class="boat-art" role="img" aria-label="Geometric boat illustration in berry tone"></div>
  <svg class="icon" style="left:234px; top:80px;" width="22" height="22" viewBox="0 0 22 22" role="img" aria-label="Sun icon">
    <g stroke="var(--white)" stroke-width="1.4" fill="none">
      <circle cx="11" cy="11" r="4.5"/>
      <path d="M11 1v3M11 18v3M1 11h3M18 11h3M4 4l2 2M16 16l2 2M4 18l2-2M16 6l2-2"/>
    </g>
  </svg>
  <h2 class="content display cruise-title">Sunset Cruise</h2>
  <p class="content cruise-sub">Post Wedding Chillax</p>
  <div class="bud" role="img" aria-label="Pink rosebud with green leaves" style="left:158px; top:248px; width:66px; height:62px;"></div>
</section>

<section class="card card--info">
  <div class="floral-wash" role="img" aria-label="Faint pink peony pattern background"></div>
  <div class="center-disc center-disc--soft" style="left:22px; top:25px; width:336px; height:320px;"></div>
  <h2 class="content display info-title">Info</h2>
  <div class="info-list">
    <p class="info-head">Dress</p>
    <p class="info-text">Smart Casual</p>
    <p class="info-head">Getting there</p>
    <p class="info-text">There will be a shuttle bus from Bo Phut to the cer&shy;emony. Please let us know if you are interested</p>
    <p class="info-head">Gifts</p>
    <p class="info-text">Your presence at our wedding is the greatest gift of all.</p>
    <p class="info-head">Champagne/Wine</p>
    <p class="info-text">Koh Samui is a tropical island where a champagne and wine can be dear. For your enjoyment and ease for the pockets we advise our guests to bring a bottle of champagne or/and wine with you</p>
    <p class="info-head">Our website</p>
    <p class="info-text">Please check for any updates or changes in our wedding site <span class="info-link">mira-tomasnearlyweds.com</span></p>
  </div>
</section>

</body>
</html>
```